Dental Co needs single page print ad

Dental company needs a 1 page ad for trade magazines.
I am uploading an example of what we want (words). We need you to make it look great. It can include people or not.
The uploaded ad isn't there to be copied, just to kind of frame what we are thinking. We are open to any design
One page ad
Size 1)

Trim Size - 8 x 10.5
Bleed Size - 8.25 x 10.75
Live Area - 7 x 10

Size 2)

Trim - 8 x 10.875
Bleed - 8.25 x 11.125
Live Area - 7 x 9.875

BRIX Brand Hex #'s

Orange - ff6319
Teal - 56b1bf
Lt. Teal - aed9da
Blue: #38394B

Target Market(s)

Dentists

Requirements
Must have
• BRIX Logo, pic of the sensor (called VANT)
Use the brand hex colors:
Orange - ff6319
Teal - 56b1bf
Lt. Teal - aed9da
Blue: #38394B

```html
<!DOCTYPE html>
<html lang="en">
<head>
<meta charset="utf-8">
<title>BRIX Imaging – VANT Sensor Ad</title>
<link rel="stylesheet" href="https://fonts.googleapis.com/css2?family=Outfit:wght@500;600;700;800&family=Quicksand:wght@400;500&display=swap">
<style>
  :root {
    --orange: #f26424;
    --lt-teal: #aedcdc;
    --white: #ffffff;
    --ink: #2b2e45;
    --brand-blue: #2e3780;
    --navy: #1b2350;
    --muted: #3a3c52;
  }
  html, body {
    margin: 0;
    padding: 0;
    width: 921px;
    height: 1200px;
    overflow: hidden;
    background: var(--white);
  }
  .ad {
    position: relative;
    width: 921px;
    height: 1200px;
    font-family: "Quicksand", sans-serif;
    color: var(--ink);
  }
  .ad__backdrop {
    position: absolute;
    left: 14px;
    top: 12px;
    width: 893px;
    height: 1173px;
    background: linear-gradient(180deg,
      var(--orange) 0%,
      var(--orange) 9%,
      var(--white) 19%,
      var(--white) 66%,
      var(--lt-teal) 84%,
      var(--lt-teal) 100%);
  }
  .headline {
    position: absolute;
    left: 0;
    width: 921px;
    top: 256px;
    margin: 0;
    text-align: center;
    font-family: "Outfit", sans-serif;
    font-weight: 700;
    font-size: 47px;
    line-height: 46px;
    letter-spacing: -0.5px;
    color: var(--orange);
    text-transform: uppercase;
  }
  .subhead {
    position: absolute;
    left: 0;
    width: 921px;
    top: 398px;
    margin: 0;
    text-align: center;
    font-family: "Outfit", sans-serif;
    font-weight: 600;
    font-size: 29px;
    color: var(--ink);
  }
  .product-name {
    position: absolute;
    left: 0;
    width: 921px;
    top: 474px;
    text-align: center;
    font-family: "Outfit", sans-serif;
    font-weight: 800;
    font-size: 50px;
    line-height: 60px;
    color: var(--brand-blue);
  }
  .pricing__divider {
    position: absolute;
    left: 466px;
    top: 541px;
    width: 2px;
    height: 83px;
    background: var(--orange);
  }
  .price {
    position: absolute;
    top: 538px;
    font-size: 22px;
    line-height: 23px;
    color: var(--muted);
  }
  .price--once { right: 479px; text-align: right; }
  .price--monthly { left: 491px; text-align: left; }
  .price__amount {
    display: block;
    font-family: "Outfit", sans-serif;
    font-weight: 700;
    font-size: 37px;
    line-height: 42px;
    color: var(--ink);
    margin-bottom: 2px;
  }
  .price__unit { font-size: 19px; }
  .sensor-image {
    position: absolute;
    left: 148px;
    top: 662px;
    width: 246px;
    height: 178px;
    border-radius: 22px;
    background: linear-gradient(160deg, #2a2d4d 0%, #4a4e72 60%, #6e7396 100%);
  }
  .features {
    position: absolute;
    left: 420px;
    top: 696px;
    margin: 0;
    padding: 0;
    list-style: none;
    font-size: 16px;
    line-height: 23.3px;
    color: var(--muted);
  }
  .features__item {
    position: relative;
    padding-left: 19px;
  }
  .features__item::before {
    content: "";
    position: absolute;
    left: 0;
    top: 7px;
    width: 10px;
    height: 10px;
    border-radius: 50%;
    background: var(--orange);
  }
  .brand {
    position: absolute;
    left: 0;
    width: 921px;
    top: 980px;
    text-align: center;
    font-family: "Outfit", sans-serif;
    font-weight: 800;
    font-size: 50px;
    line-height: 60px;
    color: var(--navy);
    letter-spacing: 1px;
  }
  .contact {
    position: absolute;
    left: 0;
    width: 921px;
    top: 1074px;
    text-align: center;
    font-family: "Outfit", sans-serif;
    font-weight: 600;
    font-size: 16px;
    line-height: 23px;
    letter-spacing: 4px;
    color: var(--ink);
  }
</style>
</head>
<body>
<main class="ad">
  <div class="ad__backdrop" role="img" aria-label="Large stylised tooth illustration in orange, white and light teal filling the background"></div>

  <h1 class="headline">A subscription option<br>for intra-oral sensors<br>is dumb.</h1>
  <p class="subhead">(until you do the math)</p>

  <div class="product-name">VANT</div>

  <div class="pricing">
    <div class="price price--once">
      <span class="price__amount">$ 1,999</span>
      one-time<br>sign up free
    </div>
    <div class="pricing__divider"></div>
    <div class="price price--monthly">
      <span class="price__amount">$139/<span class="price__unit">Month</span></span>
      Cancel<br>any time
    </div>
  </div>

  <div class="sensor-image" role="img" aria-label="Product photo of the VANT intra-oral sensor with cable"></div>

  <ul class="features">
    <li class="features__item">Lifetime $0 deductible warranty</li>
    <li class="features__item">Unlimited support &amp; upgrades</li>
    <li class="features__item">Direct integration w/ all major software</li>
    <li class="features__item">Affordable enough for every op</li>
    <li class="features__item">Preserve your capital</li>
  </ul>

  <div class="brand">BRIX IMAGING</div>
  <div class="contact">www.briximaging.com<br>(555) 014-BRIX</div>
</main>
</body>
</html>
```